Proposal Brochure for Shopfitting / Construction company

We require a proposal document (Business Capabilities) to give to customers who we are tendering to, to tell them about our business. We are a shopfitting company who complete design, fit out, project management and joinery manufacture. Please see our website www.kelvarnfit.com.au and use information in that. The document needs to be editable so that we can add to it. An editable template would be great. You can use a mix of our photos and stock photos if you like. Please use our logo colours. Orange, gray, black white so that it all ties in. We use Publisher and Powerpoint.

Target Market(s)

Commerical Builders, Retailers, Business

Industry/Entity Type

Construction Company

Font styles to use
Sans Serif

Colors
f37122
f68d4d
333333
5c5c5c
9d9d9d

Requirements
Must have
• Must have logo, relevant photos, use logo colours Orange, black, gray. Can you stock photos or Ones provided. Business Proposal document, about us, capabiities, services etc. Use content from our website
Nice to have
• Template to be editable

```html
<!DOCTYPE html>
<html lang="en">
<head>
<meta charset="utf-8">
<title>Kelvarn Fit Australia – Capabilities Brochure</title>
<link rel="stylesheet" href="https://fonts.googleapis.com/css2?family=Oswald:wght@400;500&family=Raleway:wght@400;500;600;700&display=swap">
<style>
:root{
  --orange:#f37122;
  --orange-soft:#f68d4d;
  --charcoal:#333333;
  --graphite:#5c5c5c;
  --ash:#9d9d9d;
  --ink:#1c1c1c;
  --paper:#ffffff;
  --mist:#f1f1f3;
  --stage:#e6e6e6;
  --body:'Raleway',sans-serif;
  --display:'Oswald',sans-serif;
}
*{box-sizing:border-box;margin:0;padding:0}
html,body{width:835px;height:1200px;overflow:hidden}
body{background:var(--stage);font-family:var(--body);color:var(--charcoal);position:relative}
.spread-label{position:absolute;left:47px;font-family:var(--display);font-size:22px;color:var(--graphite);letter-spacing:.5px}
.spread{position:absolute;left:47px;width:740px;height:523px;display:flex;box-shadow:0 6px 18px rgba(0,0,0,.18)}
.page{position:relative;width:370px;height:523px;overflow:hidden;background:var(--paper)}
.page svg.bg{position:absolute;inset:0;width:100%;height:100%}
.page + .page{box-shadow:inset 6px 0 10px -6px rgba(0,0,0,.25)}
.abs{position:absolute}

/* brand name */
.brand{font-family:var(--body);font-weight:600;letter-spacing:3px;text-transform:uppercase;display:flex;align-items:center;gap:8px}
.brand-mark{width:12px;height:12px;background:var(--orange)}
.brand--dark{color:var(--charcoal);font-size:17px}
.brand--light{color:var(--paper);font-size:15px}

/* outside */
.headline{font-family:var(--display);font-weight:400;color:var(--orange);font-size:32px;line-height:1;letter-spacing:2px;text-transform:uppercase}
.headline span{display:block}
.headline .rule{width:70px;height:1px;background:var(--orange);margin:7px 0 7px 20px}
.tagline{color:var(--paper);font-size:11px;line-height:1.5;text-align:center;font-weight:500}
.site{font-size:11px;letter-spacing:4px;color:var(--orange);font-weight:500}
.contact{color:var(--orange);font-size:9px;line-height:1.35;display:flex;gap:7px;margin-bottom:7px;font-weight:500}
.contact svg{flex:none;width:9px;height:9px;margin-top:1px}

/* inside */
.about-title{font-family:var(--display);font-size:22px;color:var(--charcoal);font-weight:400}
.about-title em{font-style:normal;color:var(--orange)}
.copy{font-size:8.2px;line-height:1.45;color:var(--graphite)}
.copy p{margin-bottom:8px}
.web-tab{background:var(--orange);color:var(--paper);font-size:8px;padding:5px 12px;letter-spacing:.5px}
.pillar{position:absolute;width:150px;text-align:center}
.pillar svg{width:30px;height:30px;display:block;margin:0 auto 2px}
.pillar h3{font-size:8px;font-weight:700;color:var(--graphite);letter-spacing:1px;margin-bottom:5px}
.pillar p{font-size:7.6px;line-height:1.45;color:var(--graphite);text-align:justify}
.web-foot{color:var(--paper);font-size:8px;letter-spacing:.5px}
</style>
</head>
<body>

<div class="spread-label" style="top:14px">Outside</div>
<section class="spread" style="top:48px" aria-label="Outside spread">

  <!-- back cover -->
  <article class="page back-cover">
    <svg class="bg" viewBox="0 0 370 523" preserveAspectRatio="none">
      <defs>
        <linearGradient id="backPhoto" x1="0" y1="0" x2="0" y2="1">
          <stop offset="0" stop-color="#2a2a2a"/><stop offset="1" stop-color="#121212"/>
        </linearGradient>
      </defs>
      <rect width="370" height="523" fill="#f4f4f6"/>
      <polygon points="370,140 370,200 140,250" fill="var(--orange)"/>
      <polygon points="0,250 140,250 370,200 370,523 0,523" fill="#222"/>
      <polygon points="0,370 370,335 370,523 0,523" fill="url(#backPhoto)" role="img" aria-label="Photo of a fitted-out café interior with a green plant wall"/>
      <polygon points="0,365 230,365 0,450" fill="var(--orange)"/>
    </svg>
    <div class="abs" style="left:185px;top:262px">
      <div class="contact"><svg viewBox="0 0 10 10"><path d="M5 0.5a3.2 3.2 0 0 0-3.2 3.2C1.8 6 5 9.5 5 9.5S8.2 6 8.2 3.7A3.2 3.2 0 0 0 5 .5zm0 4.5a1.3 1.3 0 1 1 0-2.6 1.3 1.3 0 0 1 0 2.6z" fill="var(--orange)"/></svg><span>24 Calder Lane, Westmore 3150<br>Victoria, Australia</span></div>
      <div class="contact"><svg viewBox="0 0 10 10"><path d="M2 .8l1.7 1.9-.9 1.3c.6 1.3 1.6 2.3 2.9 2.9l1.3-.9 1.9 1.7-1 1.5C4.4 9 1 5.6.5 2z" fill="var(--orange)"/></svg><span>(03) 9555 0142</span></div>
      <div class="contact"><svg viewBox="0 0 10 10"><rect x=".6" y="2" width="8.8" height="6" fill="none" stroke="var(--orange)" stroke-width="1"/><path d="M.6 2l4.4 3.4L9.4 2" fill="none" stroke="var(--orange)" stroke-width="1"/></svg><span>helpdesk@kelvarnfit.com.au</span></div>
    </div>
    <div class="abs brand brand--light" style="left:40px;top:315px"><span class="brand-mark"></span>Kelvarn Fit</div>
    <div class="abs site" style="left:150px;top:490px">www.kelvarnfit.com</div>
  </article>

  <!-- front cover -->
  <article class="page front-cover">
    <svg class="bg" viewBox="0 0 370 523" preserveAspectRatio="none">
      <defs>
        <linearGradient id="frontPhoto" x1="0" y1="0" x2="0" y2="1">
          <stop offset="0" stop-color="#303030"/><stop offset="1" stop-color="#141414"/>
        </linearGradient>
      </defs>
      <rect width="370" height="523" fill="#f4f4f6"/>
      <polygon points="0,100 370,70 370,523 0,523" fill="#232323"/>
      <polygon points="0,100 210,108 0,160" fill="var(--orange)"/>
      <polygon points="370,215 370,290 250,290" fill="var(--orange)"/>
      <rect x="0" y="300" width="370" height="223" fill="url(#frontPhoto)" role="img" aria-label="Photo of a dark retail interior with textured feature walls"/>
    </svg>
    <div class="abs brand brand--dark" style="left:100px;top:40px"><span class="brand-mark"></span>Kelvarn Fit</div>
    <div class="abs headline" style="left:95px;top:118px">
      <span>Inspired</span><div class="rule"></div>
      <span>Creative</span><div class="rule"></div>
      <span>Functional</span>
    </div>
    <p class="abs tagline" style="left:30px;top:335px;width:320px">We have the expertise, range of services and reputation<br>for successfully completing projects throughout Australia<br>&amp; New Zealand.</p>
    <div class="abs" style="left:150px;top:386px;width:80px;height:1px;background:var(--orange)"></div>
    <div class="abs site" style="left:175px;top:440px">www.kelvarnfit.com</div>
  </article>
</section>

<div class="spread-label" style="top:593px">Inside</div>
<section class="spread" style="top:627px" aria-label="Inside spread">

  <!-- about page -->
  <article class="page about-page">
    <svg class="bg" viewBox="0 0 370 523" preserveAspectRatio="none">
      <defs>
        <linearGradient id="shopPhoto" x1="0" y1="0" x2="1" y2="1">
          <stop offset="0" stop-color="#d9d9dc"/><stop offset=".55" stop-color="#6b5a4a"/><stop offset="1" stop-color="#2e2a26"/>
        </linearGradient>
      </defs>
      <polygon points="30,14 80,14 80,24 30,24" fill="var(--graphite)"/>
      <polygon points="85,14 370,40 370,50 85,24" fill="var(--orange)"/>
      <polygon points="0,340 370,300 370,523 0,523" fill="url(#shopPhoto)" role="img" aria-label="Photo of a completed café shopfront with glazed frontage and outdoor seating"/>
    </svg>
    <h2 class="abs about-title" style="left:30px;top:40px">About <em>Kelvarn Fit Australia</em></h2>
    <div class="abs copy" style="left:30px;top:80px;width:310px">
      <p>For over 25 years our team at Kelvarn Fit Australia have been committed to delivering shopfitting projects with highest level of attention to detail and customer service.</p>
      <p>Kelvarn Fit Australia provides the complete project experience, from design, engineering construction, installation &amp; completion, at a competitive price.</p>
      <p>Our highly consultative approach ensures that you are informed every step of the way. We would value the opportunity to tender your next project. With our extensive range of contacts across Australia and New Zealand, we can meet the needs of any fitout project, no matter the size or the location.</p>
      <p style="width:150px">Kelvarn Fit Australia have the expertise, range of services and reputation for successfully completing projects throughout Australia &amp; New Zealand.</p>
    </div>
    <div class="abs web-tab" style="left:0;top:490px">www.kelvarnfit.com</div>
  </article>

  <!-- mission page -->
  <article class="page values-page">
    <svg class="bg" viewBox="0 0 370 523" preserveAspectRatio="none">
      <defs>
        <linearGradient id="storePhoto" x1="0" y1="0" x2="1" y2="0">
          <stop offset="0" stop-color="#2b2b2b"/><stop offset=".6" stop-color="#4a4538"/><stop offset="1" stop-color="#1d1d1d"/>
        </linearGradient>
      </defs>
      <rect width="370" height="523" fill="var(--mist)"/>
      <polygon points="0,230 370,150 370,400 0,400" fill="#e8e8eb"/>
      <polygon points="0,6 370,36 370,46 0,16" fill="var(--orange)"/>
      <polygon points="320,46 370,38 370,56 320,56" fill="var(--graphite)"/>
      <polygon points="0,405 370,405 370,523 0,523" fill="url(#storePhoto)" role="img" aria-label="Photo of a fitted-out retail store at night with lit signage"/>
    </svg>

    <div class="pillar" style="left:20px;top:60px">
      <svg viewBox="0 0 30 30"><circle cx="14" cy="16" r="11" fill="none" stroke="var(--orange)" stroke-width="2"/><circle cx="14" cy="16" r="6" fill="none" stroke="var(--orange)" stroke-width="2"/><circle cx="14" cy="16" r="2" fill="var(--orange)"/><path d="M14 16L26 4M22 4h4v4" fill="none" stroke="var(--orange)" stroke-width="2"/></svg>
      <h3>MISSION</h3>
      <p>Our aim is to provide all of our clients with piece of mind and confidence in having chosen us to deliver their store. Our director and staff have successfully completed thousands of projects nationally over 25 years, we are able to provide many valuable benefits which go beyond just shopfitting.</p>
    </div>

    <div class="pillar" style="left:200px;top:95px">
      <svg viewBox="0 0 30 30"><path d="M2 15C7 7 23 7 28 15 23 23 7 23 2 15z" fill="none" stroke="var(--orange)" stroke-width="2"/><circle cx="15" cy="15" r="4.5" fill="none" stroke="var(--orange)" stroke-width="2"/><circle cx="15" cy="15" r="1.6" fill="var(--orange)"/></svg>
      <h3>VISION</h3>
      <p>Our focus on quality and service delivery is at the forefront of every project. Kelvarn Fit Australia offers a full range of specially selected services to ensure we are able to seamlessly complete your project. We can meet any fitout project no matter the size or the location, from concept to completion.</p>
    </div>

    <div class="pillar" style="left:20px;top:225px">
      <svg viewBox="0 0 30 30"><rect x="5" y="5" width="16" height="21" fill="none" stroke="var(--orange)" stroke-width="2"/><path d="M9 11h8M9 15h8M9 19h5" stroke="var(--orange)" stroke-width="1.6"/><circle cx="22" cy="21" r="5.5" fill="var(--mist)" stroke="var(--orange)" stroke-width="2"/><path d="M22 18v3h2" fill="none" stroke="var(--orange)" stroke-width="1.5"/></svg>
      <h3>HISTORY</h3>
      <p>Kelvarn Fit Australia's Director has been in the Shopfitting and Retail Maintenance business for over 25 years. During this time he has gained a reputation for excellence in service, workmanship, construction, design and for a can do attitude to ensure all projects are a success.</p>
    </div>

    <div class="pillar" style="left:200px;top:265px">
      <svg viewBox="0 0 30 30"><path d="M9 4h12v7a6 6 0 0 1-12 0z" fill="none" stroke="var(--orange)" stroke-width="2"/><path d="M9 7H5c0 4 2 6 4 6M21 7h4c0 4-2 6-4 6M15 17v5M10 26h10M12 22h6" fill="none" stroke="var(--orange)" stroke-width="2"/></svg>
      <h3>ACHIEVEMENTS</h3>
      <p>Our company and directors are long standing members of the Retail Interiors Guild (RIG), the Trade Builders Council and many other key industry bodies to ensure we are abreast of all building regulations, safety, innovation and industry best practice.</p>
    </div>

    <div class="abs web-foot" style="right:20px;top:500px">www.kelvarnfit.com</div>
  </article>
</section>

</body>
</html>
```